Web Design Project

Psychotherapist in Private Practice
Practice name "The Steady Harbor"
The population is professional adults seeking life coaching and change consultation
I am including a photo for inspiration ONLY - It includes the theme of light and tree branches. There does not HAVE to be a photograph . An illustration , concept or theme of nature /light / generativity / growth / creativity is acceptable
Clean sharp lines Light colors, minimalist , modern.
There is a separate project for a logo design that will become part of the web design
Here are examples of two logos/websites I like
http://www.quietrivergroup.example/
http://www.brightknollpartners.example/

Target Market(s)

Professional adults seeking life coaching

Industry/Entity Type

Life Coaching

Requirements
Should not have
• Although the business name has 'compassion' in it, designs with hearts in it would have to be pretty stylish, subtle, mature and sophisticated to be considered.

```html
<!DOCTYPE html>
<html lang="en">
<head>
<meta charset="utf-8">
<title>The Steady Harbor</title>
<link href="https://fonts.googleapis.com/css2?family=Mulish:wght@300;400;600;700&display=swap" rel="stylesheet">
<style>
:root{
  --wood-light:#e2bb8f;
  --wood-mid:#d3a574;
  --wood-dark:#c08d5c;
  --paper:#f2e9cd;
  --paper-edge:#ece1c1;
  --lime:#8cc63f;
  --lime-bright:#a6dc3c;
  --text:#4e4a44;
  --rule:#cfc4a6;
  --white:#ffffff;
}
*{margin:0;padding:0;box-sizing:border-box}
html,body{width:1000px;height:1200px;overflow:hidden}
body{
  position:relative;
  font-family:"Mulish",sans-serif;
  background:linear-gradient(180deg,var(--paper) 0%,var(--paper-edge) 100%);
  color:var(--text);
}
.site-header{
  position:absolute;left:0;top:0;width:1000px;height:298px;
  background:linear-gradient(90deg,var(--wood-mid),var(--wood-light) 30%,var(--wood-mid) 60%,var(--wood-light) 85%,var(--wood-mid));
  border-bottom:3px solid var(--lime);
}
.brand{position:absolute;left:104px;top:20px;display:flex;align-items:center;gap:10px}
.brand-dot{width:48px;height:48px;border-radius:50%;background:var(--white)}
.brand-name{font-size:17px;font-weight:700;color:var(--white);text-transform:uppercase;letter-spacing:-.2px}
.main-nav a,.footer-nav a{position:absolute;text-decoration:none;font-size:13px;color:var(--lime-bright);text-shadow:0 1px 1px rgba(0,0,0,.35)}
.main-nav a{top:37px}
.main-nav a.current,.footer-nav a.current{color:var(--white)}
.hero{
  position:absolute;left:102px;top:83px;width:796px;height:293px;
  background:var(--white);padding:7px 8px 8px 10px;
  box-shadow:0 14px 16px -10px rgba(0,0,0,.35);
}
.hero-visual{
  position:relative;width:100%;height:100%;
  background:linear-gradient(180deg,#f6c640 0%,#fde98a 38%,#f4c35a 52%,#6f5b4f 64%,#4d4346 100%);
  overflow:hidden;
}
.hero-caption{
  position:absolute;left:0;bottom:0;width:100%;height:65px;
  background:rgba(45,40,42,.7);
  font-size:30px;font-weight:300;color:var(--white);
  padding:12px 0 0 26px;
}
.hero-caption em{font-style:normal;color:var(--lime-bright)}
.section-label{position:absolute;left:125px;font-size:11px;font-weight:600;color:var(--lime)}
.rule{position:absolute;left:103px;width:795px;height:1px;background:var(--rule);box-shadow:0 1px 0 rgba(255,255,255,.6)}
.intro{
  position:absolute;left:126px;top:433px;width:780px;
  font-size:13.5px;font-weight:300;line-height:29px;letter-spacing:.35px;
}
.intro a{color:var(--lime);font-weight:700;text-decoration:none;font-size:11.5px;letter-spacing:.6px;margin-left:6px}
.features{position:absolute;top:657px;list-style:none}
.features li{font-size:11.5px;font-weight:700;letter-spacing:.4px;height:33.4px;display:flex;align-items:center;gap:9px}
.features svg{width:8px;height:9px}
.gallery-item{
  position:absolute;top:821px;width:250px;height:208px;background:var(--white);padding:5px;
}
.gallery-item div{width:100%;height:100%}
.cta{
  position:absolute;left:429px;top:1066px;width:142px;height:35px;
  background:var(--lime-bright);color:var(--white);
  font-size:13px;font-weight:600;text-align:center;line-height:35px;text-decoration:none;
  border-bottom:2px solid #8fc12c;
}
.site-footer{
  position:absolute;left:0;top:1144px;width:1000px;height:56px;
  background:linear-gradient(90deg,var(--wood-dark),var(--wood-light) 40%,var(--wood-mid) 75%,var(--wood-dark));
  border-top:2px solid #e6dcc0;
}
.footer-nav a{top:18px}
.copyright{position:absolute;right:107px;top:18px;font-size:13px;color:var(--white);text-shadow:0 1px 1px rgba(0,0,0,.35)}
</style>
</head>
<body>
<header class="site-header">
  <div class="brand"><span class="brand-dot"></span><span class="brand-name">The Steady Harbor</span></div>
  <nav class="main-nav">
    <a class="current" href="#" style="left:467px">Home</a>
    <a href="#" style="left:538px">About</a>
    <a href="#" style="left:612px">Services</a>
    <a href="#" style="left:697px">Events</a>
    <a href="#" style="left:771px">Contact</a>
    <a href="#" style="left:852px">Find Us</a>
  </nav>
</header>

<section class="hero">
  <div class="hero-visual" role="img" aria-label="Sunset over the sea beneath tree branches, with a smiling woman resting on her arms">
    <div class="hero-caption"><em>Life coaching</em> and consultation</div>
  </div>
</section>

<p class="section-label" style="top:401px">What we do &amp; how we can help you...</p>
<div class="rule" style="top:427px"></div>
<div class="intro">
  <p>Lorem ipsum dolor sit amet, consectetur adipiscing elit. In aliquet malesuada ultrices. Vivamus varius, nisl et placerat rhoncus, augue nisi lobortis nunc, sit amet sagittis tortor sem eu tellus. Cum sociis natoque penatibus et magnis dis parturient montes, nascetur ridiculus mus.</p>
  <p>Dum sociis natoque penatibus et magnis dis parturient montes, nascetur ridiculus musullam at leo leom Integer vitae imperdiet nunc. Nulla lacus nulla, ultrices quis sem ut. <a href="#">CONTACT US &gt;</a></p>
</div>

<p class="section-label" style="top:610px">List of features &amp; services...</p>
<div class="rule" style="top:636px"></div>

<ul class="features" style="left:125px">
  <li><svg viewBox="0 0 8 9"><path d="M1 0.5 5.5 4.5 1 8.5" fill="none" stroke="#8cc63f" stroke-width="2"/></svg>Lorem ipsum dolor sit amet</li>
  <li><svg viewBox="0 0 8 9"><path d="M1 0.5 5.5 4.5 1 8.5" fill="none" stroke="#8cc63f" stroke-width="2"/></svg>Sectetur adipiscing elitn aliquet</li>
  <li><svg viewBox="0 0 8 9"><path d="M1 0.5 5.5 4.5 1 8.5" fill="none" stroke="#8cc63f" stroke-width="2"/></svg>Vivamus varius nisl et placerat</li>
  <li><svg viewBox="0 0 8 9"><path d="M1 0.5 5.5 4.5 1 8.5" fill="none" stroke="#8cc63f" stroke-width="2"/></svg>Im sociis natoque penatibus</li>
</ul>
<ul class="features" style="left:402px">
  <li><svg viewBox="0 0 8 9"><path d="M1 0.5 5.5 4.5 1 8.5" fill="none" stroke="#8cc63f" stroke-width="2"/></svg>Donec ut molestie elit.</li>
  <li><svg viewBox="0 0 8 9"><path d="M1 0.5 5.5 4.5 1 8.5" fill="none" stroke="#8cc63f" stroke-width="2"/></svg>Duis in dictum ligula id volutpat</li>
  <li><svg viewBox="0 0 8 9"><path d="M1 0.5 5.5 4.5 1 8.5" fill="none" stroke="#8cc63f" stroke-width="2"/></svg>Aliquam erat volutpat.</li>
  <li><svg viewBox="0 0 8 9"><path d="M1 0.5 5.5 4.5 1 8.5" fill="none" stroke="#8cc63f" stroke-width="2"/></svg>Curabitur vestibulum luctus mal</li>
</ul>
<ul class="features" style="left:675px">
  <li><svg viewBox="0 0 8 9"><path d="M1 0.5 5.5 4.5 1 8.5" fill="none" stroke="#8cc63f" stroke-width="2"/></svg>Lorem ipsum dolor sit amet</li>
  <li><svg viewBox="0 0 8 9"><path d="M1 0.5 5.5 4.5 1 8.5" fill="none" stroke="#8cc63f" stroke-width="2"/></svg>Sectetur adipiscing elitn aliquet</li>
  <li><svg viewBox="0 0 8 9"><path d="M1 0.5 5.5 4.5 1 8.5" fill="none" stroke="#8cc63f" stroke-width="2"/></svg>Vivamus varius nisl et placerat</li>
  <li><svg viewBox="0 0 8 9"><path d="M1 0.5 5.5 4.5 1 8.5" fill="none" stroke="#8cc63f" stroke-width="2"/></svg>Im sociis natoque penatibus</li>
</ul>

<figure class="gallery-item" style="left:104px">
  <div role="img" aria-label="Woman stretching on a lakeside shore" style="background:linear-gradient(180deg,#e7efef 0%,#b9c9b4 30%,#9fbcc6 55%,#f0e6dc 100%)"></div>
</figure>
<figure class="gallery-item" style="left:375px">
  <div role="img" aria-label="Group of friends embracing in a bright room" style="background:linear-gradient(135deg,#eef1f4 0%,#cfd4da 45%,#5b5a66 100%)"></div>
</figure>
<figure class="gallery-item" style="left:646px">
  <div role="img" aria-label="Counsellor seated with a notepad" style="background:linear-gradient(180deg,#cfe3ea 0%,#e7dccb 55%,#d6c3a8 100%)"></div>
</figure>

<a class="cta" href="#">CONTACT US</a>

<footer class="site-footer">
  <nav class="footer-nav">
    <a class="current" href="#" style="left:105px">Home</a>
    <a href="#" style="left:176px">About</a>
    <a href="#" style="left:250px">Services</a>
    <a href="#" style="left:335px">Events</a>
    <a href="#" style="left:408px">Contact</a>
    <a href="#" style="left:490px">Find Us</a>
  </nav>
  <p class="copyright">© 2012 Company Name</p>
</footer>
</body>
</html>
```